Pictures required on web page

I would like change three existing pictures on my new website.

The site can be found here:
http://mossbottleroom.kestrelweb.com.au/

The three pictures to be changed are on the home page:
Purchase- Mixed Packs
Wine Club - Let Us Choose
Education- Wine Courses

I would like somthing stylish, classic and understated that fits in with the theme and feel of the site. I know stylish is a subjective thing. At the moment, the current picture makes the text difficult to read on a destop. Plus I don't think they are a perfect fit for our website anyway. I've attached a photo of our wine course room and also me in the store. Please, don't feel as though you have to use these pictures, but they're there if you want them. However I'm open to completely different photos/graphics to be used.

```html
<!DOCTYPE html>
<html lang="en">
<head>
<meta charset="utf-8">
<title>Mossbottle – Small winery specialist</title>
<link href="https://fonts.googleapis.com/css2?family=Roboto+Slab:wght@300;700&family=Roboto:wght@400;500&family=Raleway:wght@300;700&display=swap" rel="stylesheet">
<style>
  :root {
    --header-navy: #243259;
    --nav-navy: #1a2139;
    --tile-red: #b24749;
    --tile-navy: #21305a;
    --white: #ffffff;
    --muted: #dfe4ee;
    --search-bg: #34477a;
    --search-border: #6f82b3;
    --divider: #3d4c75;
    --overlay: rgba(255,255,255,0.12);
    --frame: rgba(255,255,255,0.45);
  }
  * { box-sizing: border-box; margin: 0; padding: 0; }
  html, body { width: 1200px; height: 639px; overflow: hidden; background: var(--white); }
  body { position: relative; font-family: "Roboto", Arial, sans-serif; color: var(--white); }

  .site-header { position: absolute; left: 0; top: 0; width: 1200px; height: 116px; background: var(--header-navy); }
  .brand { position: absolute; left: 56px; top: 22px; }
  .brand-name { font-family: "Roboto Slab", Georgia, serif; font-weight: 700; font-size: 42px; line-height: 48px; }
  .brand-tagline { font-family: "Roboto Slab", Georgia, serif; font-weight: 300; font-size: 19px; line-height: 22px; }

  .search { position: absolute; left: 365px; top: 38px; width: 320px; height: 38px; background: var(--search-bg);
            border: 1px solid var(--search-border); border-radius: 3px; }
  .search-label { position: absolute; left: 14px; top: 9px; font-size: 16px; color: #b9c4de; }
  .search svg { position: absolute; right: 10px; top: 7px; }

  .utility-nav { position: absolute; left: 718px; top: 30px; display: flex; }
  .utility-link { width: 88px; height: 48px; display: flex; flex-direction: column; align-items: center; justify-content: flex-end;
                  font-size: 13px; letter-spacing: .3px; border-left: 1px solid var(--divider); }
  .utility-link:first-child { border-left: none; }
  .utility-link svg { margin-bottom: 6px; }

  .main-nav { position: absolute; left: 0; top: 116px; width: 1200px; height: 54px; background: var(--nav-navy); }
  .main-nav ul { list-style: none; display: flex; position: absolute; left: 57px; top: 16px; }
  .main-nav li { font-size: 19px; margin-right: 33px; }
  .cart { position: absolute; left: 980px; top: 15px; display: flex; align-items: center; font-size: 14px; }
  .cart svg { margin-right: 10px; }

  .tile { position: absolute; overflow: hidden; }
  .tile-photo { position: absolute; inset: 0; }
  .caption { position: absolute; background: var(--overlay); border: 1px solid var(--frame); text-align: center;
             font-family: "Raleway", Arial, sans-serif; display: flex; flex-direction: column; justify-content: center; }
  .caption-kicker { font-weight: 700; font-size: 27px; line-height: 30px; }
  .caption-title { font-weight: 300; font-size: 36px; line-height: 40px; }

  .tile-education { left: 35px; top: 186px; width: 361px; height: 242px; }
  .tile-education .tile-photo { background: linear-gradient(120deg, #b07a45 0%, #8c5a36 40%, #b89aa2 75%, #6e4a38 100%); }
  .tile-education .caption { left: 25px; top: 73px; width: 319px; height: 104px; }

  .tile-club { left: 418px; top: 186px; width: 362px; height: 418px; }
  .tile-club .tile-photo { background: linear-gradient(160deg, #9a4a2c 0%, #5a1d22 35%, #7b5a5a 60%, #3c4a78 100%); }
  .tile-club .caption { left: 25px; top: 287px; width: 317px; height: 100px; }

  .tile-packs { left: 802px; top: 186px; width: 361px; height: 242px; }
  .tile-packs .tile-photo { background: linear-gradient(100deg, #2b2a33 0%, #4a3d35 45%, #8a6a4a 75%, #c9a887 100%); }
  .tile-packs .caption { left: 25px; top: 67px; width: 313px; height: 112px; }

  .tile-shipping { left: 35px; top: 443px; width: 361px; height: 163px; background: var(--tile-red); }
  .tile-newsletter { left: 802px; top: 441px; width: 361px; height: 162px; background: var(--tile-navy); }
  .promo-frame { position: absolute; left: 22px; top: 24px; width: 317px; height: 113px; border: 1px solid var(--frame);
                 display: flex; flex-direction: column; align-items: center; justify-content: center; font-family: "Roboto", Arial, sans-serif; }
  .promo-title { font-size: 21px; letter-spacing: 2.6px; line-height: 28px; }
  .promo-sub { font-size: 14.5px; letter-spacing: 1.3px; color: var(--muted); }
</style>
</head>
<body>
  <header class="site-header">
    <div class="brand">
      <div class="brand-name">Mossbottle</div>
      <div class="brand-tagline">Small winery specialist.</div>
    </div>
    <div class="search">
      <span class="search-label">Search the Cellars</span>
      <svg width="24" height="24" viewBox="0 0 24 24" fill="none" stroke="#fff" stroke-width="2"><circle cx="10" cy="10" r="7"/><line x1="15" y1="15" x2="22" y2="22" stroke-width="3"/></svg>
    </div>
    <nav class="utility-nav">
      <div class="utility-link"><svg width="18" height="16" viewBox="0 0 18 16" fill="#fff"><path d="M9 0 0 8h3v8h4v-5h4v5h4V8h3z"/></svg>HOME</div>
      <div class="utility-link"><svg width="24" height="18" viewBox="0 0 24 18" fill="#fff"><circle cx="12" cy="5" r="4"/><circle cx="4.5" cy="6" r="3"/><circle cx="19.5" cy="6" r="3"/><path d="M5 18c0-5 3-8 7-8s7 3 7 8z"/><path d="M0 16c0-4 2-6 4.5-6 1 0 2 .3 2.5 1-1.5 1.3-2.5 3-2.7 5z"/><path d="M24 16c0-4-2-6-4.5-6-1 0-2 .3-2.5 1 1.5 1.3 2.5 3 2.7 5z"/></svg>ABOUT</div>
      <div class="utility-link"><svg width="18" height="18" viewBox="0 0 18 18" fill="none" stroke="#fff" stroke-width="2"><rect x="1" y="3" width="16" height="14"/><line x1="1" y1="7" x2="17" y2="7"/><line x1="5" y1="0" x2="5" y2="4"/><line x1="13" y1="0" x2="13" y2="4"/></svg>EVENTS</div>
      <div class="utility-link"><svg width="18" height="18" viewBox="0 0 18 18"><circle cx="9" cy="9" r="6" fill="none" stroke="#fff" stroke-width="4" stroke-dasharray="3 1.7"/><circle cx="9" cy="9" r="5" fill="#fff"/><circle cx="9" cy="9" r="2" fill="#243259"/></svg>ACCOUNT</div>
      <div class="utility-link"><svg width="16" height="16" viewBox="0 0 16 16" fill="#fff"><path d="M3 0l3 4-2 2c1 2 4 5 6 6l2-2 4 3-2 3C7 16 0 9 0 3z"/></svg>CONTACT</div>
    </nav>
  </header>

  <nav class="main-nav">
    <ul>
      <li>Red Wine</li><li>White Wine</li><li>Sparkling</li><li>Rosé</li><li>Old &amp; Rare</li><li>Stickies</li><li>Imported</li><li>Wine Club</li>
    </ul>
    <div class="cart">
      <svg width="26" height="22" viewBox="0 0 26 22" fill="#fff"><path d="M0 0h5l1 3h20l-3 10H8l1 3h14v2H8L3 2H0z"/><circle cx="10" cy="20" r="2"/><circle cx="21" cy="20" r="2"/></svg>
      Shopping cart is empty
    </div>
  </nav>

  <section class="tile tile-education">
    <div class="tile-photo" role="img" aria-label="Photo of a winemaker holding a bottle beside oak barrels in a cellar"></div>
    <div class="caption"><span class="caption-kicker">EDUCATION</span><span class="caption-title">WINE COURSES</span></div>
  </section>

  <section class="tile tile-club">
    <div class="tile-photo" role="img" aria-label="Photo of hands raising glasses of red wine in a toast"></div>
    <div class="caption"><span class="caption-kicker">WINE CLUB</span><span class="caption-title">LET US CHOOSE</span></div>
  </section>

  <section class="tile tile-packs">
    <div class="tile-photo" role="img" aria-label="Photo of a hand taking a wine bottle from a shop shelf"></div>
    <div class="caption"><span class="caption-kicker">PURCHASE</span><span class="caption-title">MIXED PACKS</span></div>
  </section>

  <section class="tile tile-shipping">
    <div class="promo-frame"><span class="promo-title">FREE SHIPPING</span><span class="promo-sub">on orders over $200</span></div>
  </section>

  <section class="tile tile-newsletter">
    <div class="promo-frame"><span class="promo-title">NEWSLETTER</span><span class="promo-sub">join the newsletter for specials</span></div>
  </section>
</body>
</html>
```